Design For Life Insurance Landing Page

Make Sure You Look At Attachments.

What we want from our design:
Light and clear design
Clear calls to action.
Clean, uncluttered design.
Space for 1500 words of content under various headings.
Incorporation of our brand colours (and suggestions for new colours that complement them)
Incorporation of logo into menu matched to page.

Some background:

We are rebranding our existing site around our new logo and coulours and want to move away from using blue heavily.

Our current site can be found here https://kestrova.co.uk/broadband/best-broadband-deals/

We will be using this competition to find someone to work with in future, our site will have around 50 landing pages in total.

https://www.pellorin.co.uk/life-insurance.htm

What we like about this page:
The header gives a clear call to action and shows the product variants clearly.
We also like the simple and clear menu.
Very clean design.

https://www.quibblestack.com/life-insurance/

Ample space for content.
Nice explainer graphics.
Clear concise design.

https://www.wendaroo.com/life-insurance

Clear calls to action
Nice use of brand colours, especially at the bottom.

Target Market(s)

Consumers in the UK

Requirements
Must have
• Use of our brand colours with suggestions to add to pallete.
• Clear calls to action.
• Clean, uncluttered design.
• Space for 1500 words of content under various headings.
• Incorporation of our brand colours (and suggestions for new colours that complement them)
• Incorporation of logo into menu matched to page.
• Must look as polished as the examples given.
Should not have
• Cluttered, messy design

```html
<!DOCTYPE html>
<html lang="en">
<head>
<meta charset="utf-8">
<title>Kestrova – Compare cheap life insurance</title>
<link rel="stylesheet" href="https://fonts.googleapis.com/css2?family=Open+Sans:wght@400;600&family=Roboto:wght@300;400;500&family=Roboto+Condensed:wght@300&family=Ubuntu:wght@400;500&display=swap">
<style>
:root{
  --top-blue:#4a8fd0;
  --sky:#0aa6ec;
  --navy:#1b2a7a;
  --join:#0f5ca6;
  --green:#7cc242;
  --green-dark:#55a51a;
  --ink:#222;
  --grey:#7a7a7a;
  --body:#6d6d6d;
  --line:#d4d4d4;
}
*{margin:0;padding:0;box-sizing:border-box}
html,body{width:1010px;height:1200px;overflow:hidden}
body{position:relative;background:#fff;font-family:"Open Sans",sans-serif;color:var(--body)}
.abs{position:absolute}

.topbar{left:0;top:0;width:1010px;height:26px;background:var(--top-blue);color:#fff;font-size:11px}
.topbar .contact{left:150px;top:6px;display:flex;gap:12px;align-items:center}
.topbar .contact span{display:flex;align-items:center;gap:5px}
.social{right:142px;top:6px;display:flex;gap:14px}
.social i{display:block;width:13px;height:13px;border-radius:50%;background:#3ec6f5}

.header{left:0;top:26px;width:1010px;height:78px;background:linear-gradient(#fff,#f3f3f3);border-top:2px solid #e6e6e6}
.brand{left:150px;top:20px;font-family:"Ubuntu",sans-serif;font-weight:400;font-size:35px;color:#3a3a3a;letter-spacing:1px}
.nav{left:420px;top:0;display:flex;height:76px}
.nav a{display:block;padding:0 17px;line-height:80px;font-family:"Roboto",sans-serif;font-size:12.5px;color:#555;text-decoration:none;letter-spacing:.3px}
.nav a.active{background:#fff;border-top:3px solid var(--green);line-height:74px;color:#444;padding:0 19px}

.hero{left:0;top:104px;width:1010px;height:338px;background:radial-gradient(ellipse at 50% 40%,#fafafa 0%,#eceef0 60%,#dfe2e5 100%)}
.hero h1{left:0;top:36px;width:1010px;text-align:center;font-family:"Ubuntu",sans-serif;font-weight:400;font-size:31px;color:#111}
.hero h1 em{font-style:normal;color:var(--green)}
.hero .lead{left:0;top:76px;width:1010px;text-align:center;font-family:"Roboto",sans-serif;font-weight:300;font-size:15px;color:#999}
.hero .hint{left:0;top:311px;width:1010px;text-align:center;font-family:"Roboto",sans-serif;font-weight:300;font-size:11.5px;color:var(--green-dark)}
.arrow{top:188px}

.card{border-radius:6px;color:#fff;box-shadow:0 8px 10px -6px rgba(0,0,0,.45)}
.card h3{font-family:"Roboto Condensed",sans-serif;font-weight:300;letter-spacing:-.5px;text-transform:uppercase}
.card p{font-family:"Roboto",sans-serif;font-weight:400}
.card .more{font-family:"Roboto",sans-serif;font-weight:500}
.card .box{position:absolute;background:linear-gradient(#d9b676,#a98449);border-radius:2px}
.card .tag{position:absolute;border-radius:0 6px 0 0}
.card.blue{left:161px;top:161px;width:196px;height:111px;background:linear-gradient(135deg,#2e8ef0,#1a4bd0)}
.card.green{left:369px;top:139px;width:269px;height:152px;background:linear-gradient(135deg,#7cd01f,#3c9a12)}
.card.red{left:655px;top:161px;width:196px;height:111px;background:linear-gradient(135deg,#c10f12,#7a0608)}
.card.small h3{position:absolute;left:14px;top:11px;font-size:17px}
.card.small p{position:absolute;left:16px;top:35px;width:152px;font-size:5.2px;line-height:7.8px}
.card.small .more{position:absolute;left:16px;top:88px;font-size:6px}
.card.small .box{left:153px;top:76px;width:31px;height:28px}
.card.small .tag{right:0;top:0;width:36px;height:36px}
.card.green h3{position:absolute;left:20px;top:17px;font-size:23px}
.card.green p{position:absolute;left:21px;top:47px;width:210px;font-size:7.4px;line-height:11.2px}
.card.green .more{position:absolute;left:21px;top:119px;font-size:8.4px}
.card.green .box{left:210px;top:103px;width:44px;height:40px}
.card.green .tag{right:0;top:0;width:50px;height:50px}
.blue .tag{background:#2f8a25}
.green .tag{background:#e07a10}
.red .tag{background:#1f6fd0}

.finder{left:0;top:442px;width:1010px;height:74px;background:linear-gradient(#f5f5f5,#e9e9e9);border-top:1px solid #fff}
.finder label{left:175px;top:23px;font-family:"Ubuntu",sans-serif;font-size:18px;color:#555}
.finder .field{left:310px;top:15px;width:385px;height:44px;border:1px solid #bbb;border-radius:22px;background:#fff;box-shadow:inset 0 2px 3px rgba(0,0,0,.08);font-size:12px;color:#666;padding:13px 22px}
.finder .go{left:718px;top:15px;width:132px;height:40px;border:1px solid #c4c4c4;border-radius:4px;background:linear-gradient(#fff,#e4e4e4);font-weight:600;font-size:11px;letter-spacing:1px;color:#444;display:flex;align-items:center;justify-content:center;gap:12px;box-shadow:0 2px 3px rgba(0,0,0,.15)}

.band{left:0;top:517px;width:1010px;height:105px;background:var(--sky);color:#fff}
.band h2{left:152px;top:31px;font-family:"Roboto",sans-serif;font-weight:300;font-size:18px;letter-spacing:-.2px}
.band h2 b{font-weight:400;color:#0b2a66}
.band p{left:152px;top:57px;font-family:"Roboto Condensed",sans-serif;font-weight:300;font-size:13px;color:#e6f6ff}
.band .join{left:731px;top:33px;width:126px;height:39px;background:var(--join);font-family:"Roboto",sans-serif;font-size:15px;display:flex;align-items:center;justify-content:center;box-shadow:0 2px 2px rgba(0,0,0,.2)}

.content h2,.content h3{font-family:"Roboto",sans-serif;font-weight:500;color:var(--navy);font-size:16.5px;letter-spacing:-.1px}
.content p{font-size:10.9px;line-height:16px;text-align:justify;letter-spacing:-.05px}
.intro{left:150px;top:650px;width:727px}
.intro h2{margin-bottom:12px}
.intro p{margin-bottom:16px}
.col{top:794px}
.col.left{left:150px;width:359px}
.col.right{left:542px;width:330px}
.col h3{margin-bottom:12px}
.col p{margin-bottom:16px}

.feature{left:0;top:1006px;width:1010px;height:194px;background:linear-gradient(90deg,#e9e7e2 0%,#dfe6e6 35%,#e3ebef 55%,#d7e5ec 100%)}
.feature .photo{left:0;top:0;width:445px;height:194px;background:linear-gradient(100deg,#e8e4dc 0%,#d6dad6 45%,#5aa99c 70%,#e4ebec 100%)}
.feature h2{left:466px;top:48px;width:400px;font-family:"Roboto",sans-serif;font-weight:300;font-size:21px;line-height:28px;color:#1a1a1a;text-transform:uppercase}
.feature p{left:467px;top:112px;width:395px;font-size:11.8px;line-height:16px;color:#777}
.feature .read{left:465px;top:176px;width:108px;height:30px;background:#fff;border-radius:3px;box-shadow:0 1px 4px rgba(0,0,0,.25);font-size:9px;letter-spacing:1.5px;color:#555;padding:14px 0 0 22px}
</style>
</head>
<body>

<div class="topbar abs">
  <div class="contact abs">
    <span><svg width="11" height="8" viewBox="0 0 11 8"><rect x=".5" y=".5" width="10" height="7" fill="none" stroke="#fff"/><path d="M.5 .5 5.5 4.5 10.5 .5" fill="none" stroke="#fff"/></svg>hello@kestrova.co.uk</span>
    <span><svg width="8" height="11" viewBox="0 0 8 11"><path d="M2 0 0 1.5C0 6 3 10 6.5 11L8 9 6 7 4.8 8C3.5 7 2.5 5 2.5 3.5L3.5 2.5Z" fill="#fff"/></svg>+(333) 041 27658</span>
  </div>
  <div class="social abs"><i></i><i></i><i></i><i></i></div>
</div>

<header class="header abs">
  <div class="brand abs">kestrova</div>
  <nav class="nav abs">
    <a href="#">HOME</a><a href="#" class="active">BANKING</a><a href="#">HEALTH</a><a href="#">BUSINESS</a><a href="#">FAQ</a><a href="#">CONTACT</a>
  </nav>
</header>

<section class="hero abs">
  <h1 class="abs">Compare <em>cheap life insurance</em></h1>
  <p class="lead abs">We compare the leading life insurance policies with prices starting from just £5 per month</p>

  <svg class="arrow abs" style="left:118px" width="18" height="34" viewBox="0 0 18 34"><path d="M16 2 3 17 16 32" fill="none" stroke="#1e9b1e" stroke-width="5"/></svg>
  <svg class="arrow abs" style="left:874px" width="18" height="34" viewBox="0 0 18 34"><path d="M2 2 15 17 2 32" fill="none" stroke="#1e9b1e" stroke-width="5"/></svg>

  <div class="card small blue abs">
    <div class="tag" role="img" aria-label="Bundle offer ribbon"></div>
    <h3>Your text here</h3>
    <p>Lorem ipsum dolor sit amet, consectetuer adipiscing elit, sed <u>diam nonummy</u> nibh euismod tincidunt ut laoreet dolore magna aliquam erat volutpat.quis nostrud exerci tation ullamcorper suscipit lobortis nisl ut aliquip ex ea commodo consequat.</p>
    <div class="more">Lorem <u>ipsum</u> dolor sit amet</div>
    <div class="box" role="img" aria-label="Parcel box icon"></div>
  </div>

  <div class="card red small abs">
    <div class="tag" role="img" aria-label="Bundle offer ribbon"></div>
    <h3>Your text here</h3>
    <p>Lorem ipsum dolor sit amet, consectetuer adipiscing elit, sed <u>diam nonummy</u> nibh euismod tincidunt ut laoreet dolore magna aliquam erat volutpat.quis nostrud exerci tation ullamcorper suscipit lobortis nisl ut aliquip ex ea commodo consequat.</p>
    <div class="more">Lorem <u>ipsum</u> dolor sit amet</div>
    <div class="box" role="img" aria-label="Parcel box icon"></div>
  </div>

  <div class="card green abs">
    <div class="tag" role="img" aria-label="Bundle offer ribbon"></div>
    <h3>Your text here</h3>
    <p>Lorem ipsum dolor sit amet, consectetuer adipiscing elit, sed <u>diam nonummy</u> nibh euismod tincidunt ut laoreet dolore magna aliquam erat volutpat.quis nostrud exerci tation ullamcorper suscipit lobortis nisl ut aliquip ex ea commodo consequat.</p>
    <div class="more">Lorem <u>ipsum</u> dolor sit amet</div>
    <div class="box" role="img" aria-label="Parcel box icon"></div>
  </div>

  <p class="hint abs">Just enter your postcode below and we can show you the best deals available in your local area</p>
</section>

<section class="finder abs">
  <label class="abs">Find My Deals :</label>
  <div class="field abs">Enter your Postcode...</div>
  <div class="go abs">SEARCH <svg width="20" height="20" viewBox="0 0 20 20"><circle cx="7.5" cy="7.5" r="6" fill="none" stroke="#555" stroke-width="1.6"/><path d="M12 12 18.5 18.5" stroke="#555" stroke-width="3"/></svg></div>
</section>

<section class="band abs">
  <h2 class="abs">A SELECTION OF THE <b>LIFE INSURANCE PROVIDERS</b> WE COMPARE</h2>
  <p class="abs">We compare the leading life insurance policies with prices starting from just £5 per month</p>
  <div class="join abs">JOIN NOW</div>
</section>

<main class="content">
  <div class="intro abs">
    <h2>Deciding what type of life insurance you need</h2>
    <p>What type of life insurance you choose depends on what best fits your needs. The two most common types of life insurance policies are level term and decreasing term.The amount you're covered for is fixed when you start paying your premiums, and it stays the same throughout the term. A guaranteed lump sum will be paid if you die during the policy term.</p>
    <p>Also known as decreasing term insurance, is commonly used to cover the outstanding balance of a standard repayment mortgage. The amount of cover reduces over the length of the policy.</p>
  </div>
  <div class="col left abs">
    <h3>Why should I take out life insurance?</h3>
    <p>By ‘dependants’, we mean anyone whose circumstances and material wellbeing would be affected by your death – for example, your partner, your children or anyone else who is financially reliant on you.</p>
    <p>Thinking about your death and its inevitable impact on your family’s circumstances is difficult – and many people simply shy away from the topic. But not doing anything could put loved ones at financial risk. That’s why it’s important to confront the issue and take out life insurance.</p>
  </div>
  <div class="col right abs">
    <h3>How does life insurance work?</h3>
    <p>In most cases, the most effective form of life insurance is called ‘term’ insurance. This type of policy pays out an agreed amount – the ‘sum insured’ – either as a lump sum or as a regular income, if you die within a specified period – known as the ‘term’.</p>
    <p>You choose the size of the pay-out and the length of the term. For example, you may decide to have cover in place until your children are grown up and have left home.</p>
  </div>
</main>

<section class="feature abs">
  <div class="photo abs" role="img" aria-label="Photo of a carer in a green uniform sitting with an elderly woman at home"></div>
  <h2 class="abs">Deciding what type of life insurance you need</h2>
  <p class="abs">What type of life insurance you choose depends on what best fits your needs. The two most common types of life insurance policies are level term and decreasing term.</p>
  <div class="read abs">READ MORE</div>
</section>

</body>
</html>
```